Stunning descriptive illustration for world's unique software

This illustration contest is linked with a product logo design and website design contests.

Software

```html
<!DOCTYPE html>
<html lang="en">
<head>
<meta charset="utf-8">
<title>Tandem – Multimedia Keys and Server Selection</title>
<link rel="stylesheet" href="https://fonts.googleapis.com/css2?family=Source+Sans+3:wght@400;600;700&family=Roboto:wght@400;500&display=swap">
<style>
  :root {
    --page: #ffffff;
    --ink: #000000;
    --window-grey: #979797;
    --window-title: #333333;
    --close-red: #c9474c;
    --panel-light: #e9e9e9;
    --key-face: #efefef;
    --key-border: #c3c3c3;
    --key-focus: #36a9e1;
    --field-text: #8a8a8a;
    --screen-black: #0d0f10;
    --dialog-grey: #282828;
    --divider: #4a4a4a;
    --accent-blue: #33b5e5;
    --header-grey: #545454;
    --dialog-text: #f2f2f2;
  }
  html, body {
    margin: 0; padding: 0; width: 1200px; height: 1000px;
    overflow: hidden; background: var(--page);
  }
  .canvas { position: relative; width: 1200px; height: 1000px; }
  .bubbles { position: absolute; inset: 0; }
  .bubble-outline { fill: var(--page); stroke: var(--ink); stroke-width: 6; stroke-linejoin: miter; }

  /* Desktop multimedia window */
  .media-window {
    position: absolute; left: 55px; top: 247px; width: 475px; height: 333px;
    background: var(--window-grey);
    font-family: "Source Sans 3", "Myriad Pro", sans-serif;
  }
  .media-window__title {
    position: absolute; left: 0; width: 490px; top: 13px; text-align: center;
    font-size: 30px; color: var(--window-title); letter-spacing: 0.6px; margin: 0; font-weight: 400;
  }
  .media-window__close {
    position: absolute; left: 431px; top: 13px; width: 38px; height: 37px;
    background: var(--close-red); color: #fff; font-size: 17px; font-weight: 700;
    display: flex; align-items: center; justify-content: center;
  }
  .media-window__body {
    position: absolute; left: 14px; top: 63px; width: 459px; height: 258px;
    background: var(--panel-light);
  }
  .target-row { position: absolute; left: 0; top: 0; width: 459px; height: 42px; }
  .target-row__label { position: absolute; left: 12px; top: 6px; font-size: 21px; color: #222; }
  .target-row__select {
    position: absolute; left: 96px; top: 2px; width: 355px; height: 36px;
    background: var(--key-face); border: 1px solid var(--key-border); box-sizing: border-box;
    font-size: 21px; color: var(--field-text); padding: 3px 0 0 13px;
  }
  .target-row__chevron { position: absolute; right: 9px; top: 11px; }
  .key {
    position: absolute; width: 109px; height: 100px; box-sizing: border-box;
    background: var(--key-face); border: 2px solid var(--key-border);
    display: flex; align-items: center; justify-content: center;
  }
  .key--focused { border-color: var(--key-focus); }

  /* Mobile server dialog */
  .phone-screen {
    position: absolute; left: 634px; top: 247px; width: 486px; height: 353px;
    background: var(--screen-black); font-family: "Roboto", sans-serif;
  }
  .phone-screen__header {
    position: absolute; left: 29px; top: 11px; font-size: 23px; color: var(--header-grey); letter-spacing: 0.8px;
  }
  .server-dialog {
    position: absolute; left: 31px; top: 37px; width: 422px; height: 288px; background: var(--dialog-grey);
  }
  .server-dialog__title {
    position: absolute; left: 21px; top: 31px; margin: 0; font-weight: 400;
    font-size: 29px; color: var(--accent-blue); letter-spacing: 0.9px;
  }
  .server-dialog__rule { position: absolute; left: 0; top: 70px; width: 422px; height: 2px; background: var(--accent-blue); }
  .server-option {
    position: absolute; left: 0; width: 422px; height: 72px;
    border-bottom: 2px solid var(--divider); box-sizing: border-box;
  }
  .server-option__name { position: absolute; left: 17px; top: 24px; font-size: 21px; color: var(--dialog-text); letter-spacing: 0.6px; }
  .server-option__radio { position: absolute; left: 365px; top: 22px; }
  .dialog-button {
    position: absolute; top: 228px; height: 64px; font-size: 18px; color: var(--dialog-text);
    display: flex; align-items: center; justify-content: center; letter-spacing: 0.8px;
  }
  .dialog-button--cancel { left: 0; top: 224px; width: 211px; border-right: 2px solid var(--divider); padding-top: 8px; box-sizing: border-box; }
  .dialog-button--ok { left: 213px; top: 224px; width: 190px; padding-top: 4px; box-sizing: border-box; }
</style>
</head>
<body>
<div class="canvas">
  <svg class="bubbles" width="1200" height="1000" viewBox="0 0 1200 1000">
    <path class="bubble-outline" d="M72,221 H528 Q565,221 565,258 V572 Q565,609 528,609 H350 L285,738 L228,609 H72 Q35,609 35,572 V258 Q35,221 72,221 Z"/>
    <path class="bubble-outline" d="M648,221 H1110 Q1147,221 1147,258 V578 Q1147,615 1110,615 H930 L863,746 L806,615 H648 Q611,615 611,578 V258 Q611,221 648,221 Z"/>
  </svg>

  <section class="media-window">
    <h1 class="media-window__title">Multimedia Keys</h1>
    <div class="media-window__close">x</div>
    <div class="media-window__body">
      <div class="target-row">
        <span class="target-row__label">Target:</span>
        <div class="target-row__select">Pellomi 5
          <svg class="target-row__chevron" width="16" height="12" viewBox="0 0 16 12"><path d="M2 2 L8 9 L14 2" fill="none" stroke="#999" stroke-width="3"/></svg>
        </div>
      </div>
      <svg width="0" height="0" style="position:absolute">
        <defs>
          <linearGradient id="icon-shade" x1="0" y1="0" x2="1" y2="1">
            <stop offset="0" stop-color="#555"/><stop offset="1" stop-color="#111"/>
          </linearGradient>
        </defs>
      </svg>
      <div class="key key--focused" style="left:4px;top:48px">
        <svg width="60" height="56" viewBox="0 0 60 56"><path d="M10 18 H21 L36 3 V53 L21 38 H10 Z" fill="url(#icon-shade)"/><path d="M42 18 Q50 28 42 38" fill="none" stroke="#111" stroke-width="5"/></svg>
      </div>
      <div class="key" style="left:118px;top:48px">
        <svg width="74" height="56" viewBox="0 0 74 56"><path d="M4 18 H15 L30 3 V53 L15 38 H4 Z" fill="url(#icon-shade)"/><path d="M36 18 Q44 28 36 38 M44 11 Q56 28 44 45 M52 4 Q68 28 52 52" fill="none" stroke="#111" stroke-width="5"/></svg>
      </div>
      <div class="key" style="left:232px;top:48px">
        <svg width="72" height="56" viewBox="0 0 72 56"><path d="M6 18 H17 L32 3 V53 L17 38 H6 Z" fill="url(#icon-shade)"/><path d="M40 22 L54 36 M54 22 L40 36" stroke="#111" stroke-width="6"/></svg>
      </div>
      <div class="key" style="left:345px;top:48px">
        <svg width="60" height="64" viewBox="0 0 60 64"><path d="M17 19 A22 22 0 1 0 43 19" fill="none" stroke="url(#icon-shade)" stroke-width="8"/><rect x="26" y="3" width="8" height="30" rx="4" fill="#111"/></svg>
      </div>
      <div class="key" style="left:4px;top:155px">
        <svg width="70" height="40" viewBox="0 0 70 40"><path d="M2 20 L34 3 V37 Z M34 20 L66 3 V37 Z" fill="url(#icon-shade)"/></svg>
      </div>
      <div class="key" style="left:118px;top:155px">
        <svg width="70" height="46" viewBox="0 0 70 46"><path d="M4 2 L40 23 L4 44 Z" fill="url(#icon-shade)"/><rect x="44" y="4" width="8" height="38" fill="#111"/><rect x="57" y="4" width="8" height="38" fill="#111"/></svg>
      </div>
      <div class="key" style="left:232px;top:155px">
        <svg width="70" height="40" viewBox="0 0 70 40"><path d="M4 3 L36 20 L4 37 Z M36 3 L68 20 L36 37 Z" fill="url(#icon-shade)"/></svg>
      </div>
      <div class="key" style="left:345px;top:155px">
        <svg width="44" height="44" viewBox="0 0 44 44"><rect x="1" y="1" width="42" height="42" fill="url(#icon-shade)"/></svg>
      </div>
    </div>
  </section>

  <section class="phone-screen">
    <div class="phone-screen__header">Tandem Server Selection</div>
    <div class="server-dialog">
      <h2 class="server-dialog__title">Tandem Server to connect</h2>
      <div class="server-dialog__rule"></div>
      <div class="server-option" style="top:80px">
        <span class="server-option__name">Office Desktop</span>
        <svg class="server-option__radio" width="26" height="26" viewBox="0 0 26 26"><circle cx="13" cy="13" r="11.5" fill="#1b1b1b" stroke="#777" stroke-width="1.5"/><circle cx="13" cy="13" r="7.5" fill="var(--accent-blue)"/></svg>
      </div>
      <div class="server-option" style="top:152px">
        <span class="server-option__name">Home Notebook</span>
        <svg class="server-option__radio" width="26" height="26" viewBox="0 0 26 26"><circle cx="13" cy="13" r="11.5" fill="none" stroke="#777" stroke-width="1.5"/></svg>
      </div>
      <div class="dialog-button dialog-button--cancel">Cancel</div>
      <div class="dialog-button dialog-button--ok">OK</div>
    </div>
  </section>
</div>
</body>
</html>
```